Vellora Labs - Mushroom Supplement Packaging

Our brand is called Vellora Labs. I've added a couple different logos that you can use. We are creating a line up of Mushroom Supplement products. I will add the entire line-up of products here. I've added examples of other products and packaging shape types I can purchase. Give me different options for packaging that is minimalist and clean for this brand that makes it look really well made and clean and make people want to buy.

Product 1 Lions Mane 1g
Product 2 Cordyceps 1g
Product 3 Chaga 1g
Product 4 Turkey Tail 1g
Product 5 Reishi 1g
Product 6 Maitake 1g
Product 7 Shiitake 1g

Product 8 (Mix) Lions Mane 143mg
Cordyceps 143mg
Chaga 143mg
Turkey Tail 143mg
Reishi 143mg
Maitake 143mg
Shiitake 143mg

```html
<!DOCTYPE html>
<html lang="en">
<head>
<meta charset="utf-8">
<title>Vellora Labs – Mushroom Extract Capsules Line-up</title>
<link rel="stylesheet" href="https://fonts.googleapis.com/css2?family=Poppins:wght@300;400;500;600;700;800&display=swap">
<style>
  :root {
    --bg: #ffffff;
    --label-white: #eeeeee;
    --ink: #1b1b1b;
    --chaga: #ea8a2c;
    --turkey-tail: #3a97e3;
    --lions-mane: #9a72c2;
    --band-text: #ffffff;
  }
  * { box-sizing: border-box; margin: 0; padding: 0; }
  html, body {
    width: 1200px;
    height: 604px;
    overflow: hidden;
    background: var(--bg);
  }
  .lineup {
    width: 1200px;
    height: 604px;
    display: flex;
    justify-content: center;
    align-items: center;
    gap: 48px;
  }
  .label {
    width: 312px;
    height: 232px;
    display: flex;
    flex-direction: column;
    background: var(--label-white);
    font-family: "Poppins", sans-serif;
  }
  .label--chaga { --accent: var(--chaga); }
  .label--turkey-tail { --accent: var(--turkey-tail); }
  .label--lions-mane { --accent: var(--lions-mane); }

  .brand-band {
    height: 88px;
    background: var(--accent);
    display: flex;
    align-items: center;
    justify-content: center;
    gap: 14px;
    color: var(--band-text);
  }
  .brand-name {
    font-weight: 600;
    font-size: 22px;
    line-height: 1;
    letter-spacing: 0.5px;
    text-transform: uppercase;
    width: 120px;
    text-align: center;
  }
  .band-divider {
    width: 1px;
    height: 42px;
    background: rgba(255,255,255,0.7);
  }
  .band-tagline {
    font-weight: 300;
    font-size: 11.5px;
    line-height: 1.12;
    letter-spacing: 0.6px;
    text-transform: uppercase;
  }

  .product-panel {
    flex: 1;
    position: relative;
    text-align: center;
    padding-top: 22px;
  }
  .product-name {
    color: var(--accent);
    font-weight: 800;
    font-size: 36px;
    line-height: 1;
    letter-spacing: 0.3px;
  }
  .product-benefit {
    margin-top: 8px;
    color: var(--ink);
    font-size: 12.5px;
    line-height: 1.15;
  }
  .product-benefit sup { font-size: 7px; }
  .supplement-note {
    position: absolute;
    left: 58px;
    bottom: 18px;
    color: var(--accent);
    font-size: 7px;
  }
  .capsule-count {
    position: absolute;
    right: 62px;
    bottom: 12px;
    display: flex;
    align-items: center;
    gap: 3px;
    color: var(--ink);
  }
  .capsule-count svg { width: 8px; height: 18px; }
  .count-text { display: flex; flex-direction: column; line-height: 1; }
  .count-number { font-weight: 600; font-size: 15px; }
  .count-unit { font-size: 5px; }
</style>
</head>
<body>
<main class="lineup">

  <section class="label label--chaga">
    <header class="brand-band">
      <span class="brand-name">Vellora Labs</span>
      <span class="band-divider"></span>
      <span class="band-tagline">Mushroom<br>Extract<br>Capsules</span>
    </header>
    <div class="product-panel">
      <h2 class="product-name">CHAGA</h2>
      <p class="product-benefit">Immune Support, Antioxidant<br>Support &amp; Digestive Health<sup>†</sup></p>
      <span class="supplement-note">Dietary Supplement</span>
      <div class="capsule-count">
        <svg viewBox="0 0 8 18" aria-hidden="true">
          <rect x="0.6" y="0.6" width="6.8" height="16.8" rx="3.4" fill="#fff" stroke="var(--ink)" stroke-width="1"/>
          <path d="M0.6 9 H7.4 V14 a3.4 3.4 0 0 1 -6.8 0 Z" fill="var(--chaga)"/>
          <rect x="0.6" y="0.6" width="6.8" height="16.8" rx="3.4" fill="none" stroke="var(--ink)" stroke-width="1"/>
        </svg>
        <span class="count-text"><span class="count-number">120</span><span class="count-unit">Capsules</span></span>
      </div>
    </div>
  </section>

  <section class="label label--turkey-tail">
    <header class="brand-band">
      <span class="brand-name">Vellora Labs</span>
      <span class="band-divider"></span>
      <span class="band-tagline">Mushroom<br>Extract<br>Capsules</span>
    </header>
    <div class="product-panel">
      <h2 class="product-name">TURKEY TAIL</h2>
      <p class="product-benefit">Immune Support &amp; Defense<sup>†</sup></p>
      <span class="supplement-note">Dietary Supplement</span>
      <div class="capsule-count">
        <svg viewBox="0 0 8 18" aria-hidden="true">
          <rect x="0.6" y="0.6" width="6.8" height="16.8" rx="3.4" fill="#fff"/>
          <path d="M0.6 9 V4 a3.4 3.4 0 0 1 6.8 0 V9 Z" fill="var(--turkey-tail)"/>
          <rect x="0.6" y="0.6" width="6.8" height="16.8" rx="3.4" fill="none" stroke="var(--ink)" stroke-width="1"/>
        </svg>
        <span class="count-text"><span class="count-number">120</span><span class="count-unit">Capsules</span></span>
      </div>
    </div>
  </section>

  <section class="label label--lions-mane">
    <header class="brand-band">
      <span class="brand-name">Vellora Labs</span>
      <span class="band-divider"></span>
      <span class="band-tagline">Mushroom<br>Extract<br>Capsules</span>
    </header>
    <div class="product-panel">
      <h2 class="product-name">LION´S MANE</h2>
      <p class="product-benefit">Focus, Clarity &amp; Mood<sup>†</sup></p>
      <span class="supplement-note">Dietary Supplement</span>
      <div class="capsule-count">
        <svg viewBox="0 0 8 18" aria-hidden="true">
          <rect x="0.6" y="0.6" width="6.8" height="16.8" rx="3.4" fill="#fff"/>
          <path d="M0.6 9 V4 a3.4 3.4 0 0 1 6.8 0 V9 Z" fill="var(--lions-mane)"/>
          <rect x="0.6" y="0.6" width="6.8" height="16.8" rx="3.4" fill="none" stroke="var(--ink)" stroke-width="1"/>
        </svg>
        <span class="count-text"><span class="count-number">120</span><span class="count-unit">Capsules</span></span>
      </div>
    </div>
  </section>

</main>
</body>
</html>
```